Business Card phone number change

This one should be easy, and I've committed to pay even is takes you minutes to complete.
I have a completed business card for which I just need a phone number changed. It needs to be done asap (within hours) so I can have it printed today. I have the card design and everything. Literally just need phone number changed and positioned in correct place. If you can do it, let me know.
The card was originally designed with 3.62” x 2.12” . It was modified to US standard 3.5” x 2” (which is how I need it).

On the file named "Final TK Partners card size" the NY number should read +1 555 318 4720" rather than the 555 407 2983 number that is there. If you can do let, let me now ASAP.
Updates

Project Deadline Extended Reason: The deadling is today, 4 hours from initial posting. Short window as all that needs to be changed is the phone number and I need to print a stack today before meeting. Added Saturday, January 14, 2017

Industry/Entity Type

Business

Requirements
Must have
• The correct NY phone number of +1 555 318 4720
• Everything else stays the same.

```html
<!DOCTYPE html>
<html lang="en">
<head>
<meta charset="utf-8">
<title>TK Partners – Business Card</title>
<link href="https://fonts.googleapis.com/css2?family=Source+Serif+4:wght@400;700&display=swap" rel="stylesheet">
<style>
  :root {
    --navy: #0d4a6b;
    --ink: #555759;
    --paper: #ffffff;
    --backdrop: #ebecec;
  }
  * { margin: 0; padding: 0; box-sizing: border-box; }
  html, body {
    width: 1200px; height: 1000px; overflow: hidden;
    background: var(--backdrop);
    font-family: "Source Serif 4", Georgia, serif;
  }
  .card {
    position: absolute; left: 327px; top: 341px;
    width: 516px; height: 294px;
    background: var(--paper);
    overflow: hidden;
  }
  .brand {
    position: absolute; right: 21px; top: 19px;
    display: flex; align-items: center; gap: 10px;
  }
  .brand-dot { width: 60px; height: 60px; display: block; }
  .brand-name {
    font-weight: 700; font-size: 26px; color: var(--navy);
    letter-spacing: 0.2px; line-height: 1;
  }
  .address {
    position: absolute; right: 21px; top: 72px;
    text-align: right; font-size: 14px; line-height: 17px; color: var(--ink);
  }
  .person { position: absolute; left: 96px; top: 119px; }
  .person-name { font-weight: 700; font-size: 20px; color: var(--navy); line-height: 24px; }
  .person-title { font-size: 17px; color: var(--ink); line-height: 20px; }
  .rule {
    position: absolute; left: 96px; right: 0; height: 4px; background: var(--navy);
  }
  .rule-top { top: 171px; }
  .rule-bottom { top: 262px; }
  .contacts {
    position: absolute; left: 0; top: 184px;
    display: grid; grid-template-columns: 88px auto; column-gap: 8px;
    font-size: 14px; line-height: 18.3px;
  }
  .contacts dt { text-align: right; color: var(--ink); }
  .contacts dd { color: var(--navy); }
</style>
</head>
<body>
  <main class="card">
    <div class="brand">
      <svg class="brand-dot" viewBox="0 0 60 60" aria-hidden="true">
        <circle cx="30" cy="30" r="30" fill="var(--navy)"/>
      </svg>
      <span class="brand-name">TK Partners</span>
    </div>
    <p class="address">48 Harbor Lane<br>Brookline, NY 11420</p>

    <div class="person">
      <h1 class="person-name">Lena Marsh</h1>
      <p class="person-title">Healthcare Consultant</p>
    </div>

    <div class="rule rule-top"></div>
    <dl class="contacts">
      <dt>New York:</dt><dd>+1 555 318 4720</dd>
      <dt>Madrid:</dt><dd>+34 611 204 857</dd>
      <dt>Email:</dt><dd>lmarsh@tkpartners.com</dd>
      <dt>Web:</dt><dd>www.tkpartners.com</dd>
    </dl>
    <div class="rule rule-bottom"></div>
  </main>
</body>
</html>
```